依頼詳細
開催日の数日前に、会場周辺ご近所のポストへチラシを投函しています。枚数は毎回10,000枚前後です。そのチラシのデザイン作成をお願い致します。ポストに入っていたチラシを見て、思わす「ん?面白そうだから気軽に一度何か持って行ってみようかな」と思ってもらえるような、あと来場される方は中高年からご年配の方がほとんどなので、安心感を与えるデザインを希望です。
記載項目

```html
<!DOCTYPE html>
<html lang="ja">
<head>
<meta charset="utf-8">
<title>無料査定会のお知らせ</title>
<link href="https://fonts.googleapis.com/css2?family=Shippori+Mincho:wght@500;700;800&family=Noto+Sans+JP:wght@400;700&display=swap" rel="stylesheet">
<style>
:root{
  --red:#c8161d;
  --ink:#2a2a2a;
  --gold:#a8842c;
  --paper:#ffffff;
  --map:#9a8c7c;
  --rule:#555;
}
*{margin:0;padding:0;box-sizing:border-box}
html,body{width:846px;height:1200px;overflow:hidden;background:var(--paper)}
.flyer{position:relative;width:846px;height:1200px;font-family:"Shippori Mincho",serif;color:var(--ink);border:2px solid #d8d0c4}
.hero-photo{position:absolute;left:28px;top:28px;width:790px;height:410px;background:radial-gradient(ellipse at 28% 55%,#fffef8 0%,#e9e3d4 35%,#c9bfae 70%,#f4efe6 100%)}
.hero-fade{position:absolute;left:380px;top:28px;width:438px;height:410px;background:linear-gradient(90deg,rgba(255,255,255,0),#fff 30%)}
.quote{position:absolute;left:262px;top:46px;font-size:39px;font-weight:700;line-height:1.35;letter-spacing:1px;white-space:nowrap}
.quote .l2{display:block;padding-left:78px}
.items{position:absolute;left:440px;top:172px;font-size:32px;font-weight:800;color:var(--red);line-height:1.24;white-space:nowrap}
.search{position:absolute;left:58px;top:322px;font-size:32px;font-weight:800;color:#fff;line-height:1.3;-webkit-text-stroke:6px #5a4a30;paint-order:stroke fill;white-space:nowrap}
.organizer{position:absolute;left:0;width:846px;top:452px;text-align:center;font-size:20px;font-weight:700;white-space:nowrap}
.organizer .brand{color:var(--red);font-size:32px;margin:0 6px;letter-spacing:1px}
.headline{position:absolute;left:0;width:846px;top:478px;text-align:center;font-size:74px;font-weight:800;color:var(--red);letter-spacing:3px;white-space:nowrap}
.lead{position:absolute;left:0;width:846px;top:580px;text-align:center;font-size:21px;line-height:1.45}
.fine{position:absolute;right:50px;top:641px;font-family:"Noto Sans JP",sans-serif;font-size:9px;color:#666}
.map{position:absolute;left:46px;top:656px;width:350px;height:356px;background:var(--map);display:flex;align-items:center;padding-left:30px;color:#fff;font-size:34px;font-weight:700}
.event{position:absolute;left:416px;top:656px;width:384px}
.event .limited{font-size:32px;font-weight:800;color:var(--red);margin-bottom:14px;white-space:nowrap}
.event .row{border-bottom:1.5px solid var(--rule);font-size:32px;font-weight:800;height:62px;line-height:62px;white-space:pre}
.event .date{padding-left:36px}
.notes{position:absolute;left:46px;top:1028px;font-family:"Noto Sans JP",sans-serif;font-size:13px;line-height:1.9}
.notes li{list-style:none}
.notes li::before{content:"■";margin-right:4px}
.phone{position:absolute;left:470px;top:1022px;width:330px;height:76px;border:2px solid var(--red);display:flex;align-items:center;justify-content:center;gap:10px;color:var(--red)}
.phone .num{font-family:"Noto Sans JP",sans-serif;font-weight:700;font-size:38px;letter-spacing:-1px}
.phone .hours{position:absolute;bottom:-2px;right:10px;font-size:11px;color:var(--ink)}
.footer{position:absolute;left:28px;right:28px;top:1108px;border-top:2px solid var(--ink);padding-top:8px;font-family:"Noto Sans JP",sans-serif;font-size:13px;display:flex;gap:24px}
</style>
</head>
<body>
<div class="flyer">
  <div class="hero-photo" role="img" aria-label="ダイヤモンドの指輪のクローズアップ写真"></div>
  <div class="hero-fade"></div>
  <p class="quote">「この指輪は、<span class="l2">ここにあったのね・・・」</span></p>
  <p class="items">金、プラチナ、ダイヤ<br>色石、指輪、ネックレス<br>切手、テレホンカード<br>古銭、記念コイン<br>時計、銀杯、銀製品<br>絵画相談など</p>
  <p class="search">押入・タンス・宝石箱…<br>探してみてください。</p>

  <p class="organizer">― 創業12年の実績<span class="brand">SUNRISE STAR</span>サンライズスター が開催する ―</p>
  <h1 class="headline">無料査定会のお知らせ</h1>
  <p class="lead">お店には入りにくい方、遺品整理に、処分してしまう前に。<br>気がついたものがございましたら、お気軽にご相談ください。</p>
  <p class="fine">※査定のみでも歓迎いたします</p>

  <div class="map" role="img" aria-label="会場周辺の地図">地図</div>
  <div class="event">
    <p class="limited">年1回/2日間の限定開催!</p>
    <p class="row date">   月  日(  )と  日(  )</p>
    <p class="row">開催時間</p>
    <p class="row">会場</p>
  </div>

  <ul class="notes">
    <li>お売りいただく際は身分証明書をお持ちください。</li>
    <li>当日ご都合の悪い方は出張買取も承ります。</li>
  </ul>
  <div class="phone">
    <svg width="40" height="40" viewBox="0 0 24 24" aria-hidden="true"><path fill="#c8161d" d="M6.6 10.8a15 15 0 0 0 6.6 6.6l2.2-2.2c.3-.3.7-.4 1-.2 1.1.4 2.3.6 3.6.6.6 0 1 .4 1 1V20c0 .6-.4 1-1 1A17 17 0 0 1 3 4c0-.6.4-1 1-1h3.5c.6 0 1 .4 1 1 0 1.3.2 2.5.6 3.6.1.3 0 .7-.2 1z"/></svg>
    <span class="num">0120-00-4821</span>
    <span class="hours">[電話受付時間 9時〜18時]</span>
  </div>
  <div class="footer">
    <span>(株式会社ミナト)</span>
    <span>〒100-0000 東京都中央区見本町1-2-3 見本ビル3F</span>
    <span>TEL 03-0000-4821</span>
  </div>
</div>
</body>
</html>
```